Business cards for education company

We need a business card design for a relatively new company based in Queensland and operating across Australia. We resell diploma level education courses which include Business, Management, Finance, Community Services & Government courses. We offer over 20 different courses.
The target market is for anyone 16 years of age and older. There is no age limit.

We would like to see the design use the color blue and silver. The final design should communicate professionalism and a bright future.

We sell education but are also promoting the career they see themselves in 2-3 years in the future

Our company logo is attached.

Target Market(s)

We target all age groups above 16 years of age. The main target market would be people aged between 17-35.

We focus on those people who cannot make it into University or do not want to commit the time to a full degree.

Industry/Entity Type

Education

Requirements
Must have
• Professional
Company logo
website
Contact details:

Please use the following example:

Lionel Tapping
Senior Education Consultant
0417 385 960
Lionel.tapping@skylarklearninghub.com.au
www.skylarklearninghub.com.au

```html
<!DOCTYPE html>
<html lang="en">
<head>
<meta charset="utf-8">
<title>Skylark Learning Hub – Business Cards</title>
<link rel="stylesheet" href="https://fonts.googleapis.com/css2?family=Bitter:wght@400;500&family=Tinos:wght@700&display=swap">
<style>
  :root {
    --stage: #e9ebee;
    --card-white: #ffffff;
    --blue-deep: #13508f;
    --blue-mid: #2c7cc1;
    --blue-light: #5fb0e6;
    --silver: #c9ced4;
    --slate: #4b5158;
    --slate-dark: #3b4046;
    --text-light: #ffffff;
  }
  * { box-sizing: border-box; margin: 0; padding: 0; }
  html, body { width: 1200px; height: 474px; overflow: hidden; }
  body {
    background: var(--stage);
    font-family: "Bitter", Georgia, serif;
    position: relative;
  }
  .card {
    position: absolute;
    top: 72px;
    width: 520px;
    height: 330px;
    border-radius: 26px;
    overflow: hidden;
    box-shadow: 0 6px 18px rgba(0,0,0,0.25);
  }

  /* Front card */
  .card-front { left: 50px; background: var(--card-white); }
  .brand {
    position: absolute;
    top: 58px; left: 0; right: 0;
    display: flex; align-items: center; justify-content: center; gap: 16px;
  }
  .brand-mark {
    width: 54px; height: 54px; border-radius: 50%;
    background: var(--blue-mid);
  }
  .brand-name {
    font-family: "Tinos", "Times New Roman", serif;
    font-weight: 700;
    font-size: 34px;
    color: var(--blue-deep);
    letter-spacing: 0.5px;
  }
  .contact-band {
    position: absolute;
    top: 158px; left: 0; right: 0; height: 112px;
    background: linear-gradient(90deg, var(--blue-mid) 0%, var(--blue-light) 55%, var(--blue-mid) 100%);
    border-top: 3px solid var(--silver);
    display: flex; flex-direction: column; align-items: center; justify-content: center; gap: 8px;
    color: var(--text-light);
    font-size: 14px;
  }
  .contact-line { display: flex; align-items: center; gap: 6px; }
  .contact-line svg { width: 13px; height: 13px; fill: var(--text-light); }
  .name-strip {
    position: absolute;
    left: 0; right: 0; bottom: 0; height: 60px;
    background: linear-gradient(180deg, var(--slate) 0%, var(--slate-dark) 100%);
    color: var(--text-light);
    display: flex; align-items: center; justify-content: center; gap: 6px;
  }
  .person-name { font-size: 22px; font-weight: 500; }
  .person-title { font-size: 14px; padding-top: 4px; }

  /* Back card */
  .card-back {
    left: 630px;
    background: radial-gradient(ellipse at 60% 50%, var(--blue-light) 0%, var(--blue-mid) 45%, var(--blue-deep) 100%);
  }
  .team-art {
    position: absolute;
    top: 40px; left: 130px; width: 320px; height: 290px;
    background: radial-gradient(ellipse at 50% 60%, rgba(20,60,110,0.35) 0%, rgba(20,60,110,0) 70%);
  }
  .back-content {
    position: absolute;
    top: 108px; left: 118px;
    color: var(--text-light);
  }
  .back-brand {
    font-family: "Tinos", "Times New Roman", serif;
    font-weight: 700;
    font-size: 42px;
    line-height: 1.05;
  }
  .back-web { margin-top: 14px; font-size: 16px; }
</style>
</head>
<body>
  <section class="card card-front" aria-label="Business card front">
    <div class="brand">
      <span class="brand-mark" aria-hidden="true"></span>
      <span class="brand-name">SKYLARK LEARNING HUB</span>
    </div>
    <div class="contact-band">
      <p class="contact-line">
        <svg viewBox="0 0 16 16" aria-hidden="true"><path d="M3.6 1.5l2.3 2.6-1.3 2a9 9 0 0 0 5.3 5.3l2-1.3 2.6 2.3-1.3 2.1C8 14.8 1.2 8 1.5 2.8z"/></svg>
        0417 385 960
      </p>
      <p class="contact-line">
        <svg viewBox="0 0 16 16" aria-hidden="true"><path d="M1 4h14v9H1z M1 4l7 5 7-5" fill="none" stroke="#fff" stroke-width="1.5"/></svg>
        Lionel.tapping@skylarklearninghub.com.au
      </p>
      <p class="contact-line">
        <svg viewBox="0 0 16 16" aria-hidden="true"><circle cx="8" cy="8" r="6.5" fill="none" stroke="#fff" stroke-width="1.5"/><path d="M1.5 8h13M8 1.5c-3 3.5-3 9.5 0 13M8 1.5c3 3.5 3 9.5 0 13" fill="none" stroke="#fff" stroke-width="1.2"/></svg>
        www.skylarklearninghub.com.au
      </p>
    </div>
    <div class="name-strip">
      <span class="person-name">Lionel Tapping,</span>
      <span class="person-title">Senior Education Consultant</span>
    </div>
  </section>

  <section class="card card-back" aria-label="Business card back">
    <div class="team-art" role="img" aria-label="Faint silhouettes of three business professionals standing"></div>
    <div class="back-content">
      <p class="back-brand">SKYLARK<br>LEARNING HUB</p>
      <p class="back-web">www.skylarklearninghub.com.au</p>
    </div>
  </section>
</body>
</html>
```